Family Ranch with a hobby vineyard needs 2 wine labels for our first harvest

Design 2 wine labels (front and back) with the Brindor Ranch logo.
Label 1:
Sauvignon Blanc
Alc. 12.5% by Vol.
Palos Verdes Peninsula - add as the region
Year 2022
Label 2:
Cabernet Sauvignon
Alc. 13.5% by Vol.
Year 2022
For the back label design:
GOVERNMENT WARNING: (1) According to the Surgeon General, women
should not drink alcoholic beverages during pregnancy because of the risk of
birth defects. (2) Consumption of alcoholic beverages impairs your ability to
drive a car or operate machinery, and may cause health problems.
Contains Sulfates.
750ML
I just received the bottles and have attached a picture.
Look and feel
Each slider illustrates characteristics of the customer's brand and the style your logo design should communicate.

```html
<!DOCTYPE html>
<html lang="en">
<head>
<meta charset="utf-8">
<title>Brindor Ranch — Sauvignon Blanc Labels</title>
<link rel="stylesheet" href="https://fonts.googleapis.com/css2?family=Jost:wght@400;500&family=Open+Sans:wght@400;700&display=swap">
<style>
  :root {
    --ink: #111111;
    --paper: #ffffff;
    --backdrop: #f2f2f0;
    --edge: #d4d4d4;
  }
  * { box-sizing: border-box; margin: 0; padding: 0; }
  html, body {
    width: 1137px;
    height: 1200px;
    overflow: hidden;
    background: var(--backdrop);
  }
  .canvas {
    position: relative;
    width: 1137px;
    height: 1200px;
    color: var(--ink);
    font-family: "Jost", sans-serif;
  }
  .label {
    position: absolute;
    background: var(--paper);
    border: 1px solid var(--edge);
    display: flex;
    flex-direction: column;
    align-items: center;
  }

  /* Front label */
  .label--front {
    left: 70px;
    top: 210px;
    width: 500px;
    height: 770px;
    padding-top: 250px;
  }
  .brand {
    display: flex;
    align-items: center;
    gap: 14px;
    font-family: "Jost", sans-serif;
    font-weight: 500;
    color: var(--ink);
    letter-spacing: 0.02em;
    white-space: nowrap;
  }
  .brand__dot {
    border-radius: 50%;
    background: var(--ink);
    flex: none;
  }
  .label--front .brand { font-size: 44px; }
  .label--front .brand__dot { width: 22px; height: 22px; }

  .varietal {
    margin-top: 100px;
    font-size: 37px;
    font-weight: 400;
    letter-spacing: 0.03em;
  }
  .abv {
    margin-top: 22px;
    font-size: 18px;
    font-weight: 400;
  }
  .region {
    margin-top: 108px;
    font-size: 24px;
    font-weight: 400;
    letter-spacing: 0.02em;
  }
  .vintage {
    margin-top: 18px;
    font-size: 24px;
    font-weight: 400;
  }

  /* Back label */
  .label--back {
    left: 680px;
    top: 300px;
    width: 380px;
    height: 580px;
    padding: 190px 24px 0;
  }
  .label--back .brand { font-size: 26px; }
  .label--back .brand__dot { width: 13px; height: 13px; }
  .warning {
    margin-top: 70px;
    font-family: "Open Sans", sans-serif;
    font-size: 11px;
    line-height: 1.4;
    text-align: left;
  }
  .warning strong { font-weight: 700; }
  .back-footer {
    position: absolute;
    left: 24px;
    right: 24px;
    bottom: 80px;
    display: flex;
    justify-content: space-between;
    font-size: 11px;
    font-weight: 400;
    letter-spacing: 0.04em;
    text-transform: uppercase;
  }
</style>
</head>
<body>
<main class="canvas">

  <section class="label label--front" aria-label="Front label">
    <div class="brand"><span class="brand__dot"></span>BRINDOR RANCH</div>
    <h1 class="varietal">SAUVIGNON BLANC</h1>
    <p class="abv">Alc. 12.5% by Vol.</p>
    <p class="region">PALOS VERDES PENINSULA</p>
    <p class="vintage">2022</p>
  </section>

  <section class="label label--back" aria-label="Back label">
    <div class="brand"><span class="brand__dot"></span>BRINDOR RANCH</div>
    <p class="warning"><strong>GOVERNMENT WARNING:</strong> (1) According to the Surgeon General, women should not drink alcoholic beverages during pregnancy because of the risk of birth defects. (2) Consumption of alcoholic beverages impairs your ability to drive a car or operate machinery, and may cause health problems.</p>
    <div class="back-footer">
      <span class="volume">750 ML</span>
      <span class="sulfites">Contains Sulfates</span>
    </div>
  </section>

</main>
</body>
</html>
```